Atelier Mirou

I am actually making my own traditional french food.
Everything is homemade with passion.
I make differente terrines, jams, macaroons, rillettes and much more
I do as well cocktail party and catering

Hello everyone,

On the business card I would like to see appear if it's possible these following informations: traditional french food, cocktail party and catering.

```html
<!DOCTYPE html>
<html lang="en">
<head>
<meta charset="utf-8">
<title>Atelier Mirou – Business Card</title>
<link href="https://fonts.googleapis.com/css2?family=Source+Sans+3:wght@400;600&display=swap" rel="stylesheet">
<style>
  :root {
    --page-bg: #ffffff;
    --card-edge: #3fb0e0;
    --ink: #231f20;
    --brand-red: #c1272d;
    --navy: #133a66;
    --orange-light: #f7941d;
    --orange-deep: #f15a24;
    --white: #ffffff;
  }
  * { box-sizing: border-box; margin: 0; padding: 0; }
  html, body {
    width: 980px;
    height: 1200px;
    overflow: hidden;
    background: var(--page-bg);
    font-family: "Source Sans 3", "Myriad Pro", sans-serif;
  }
  .card {
    position: absolute;
    border: 1.5px solid var(--card-edge);
    border-radius: 18px;
    overflow: hidden;
    background: var(--white);
  }
  .card--front { left: 16px; top: 16px; width: 896px; height: 555px; }
  .card--back  { left: 32px; top: 653px; width: 896px; height: 517px; }

  .identity {
    position: absolute;
    display: flex;
    flex-direction: column;
    align-items: center;
    transform: translate(-50%, -50%);
    color: var(--ink);
    white-space: nowrap;
  }
  .brand {
    display: flex;
    align-items: center;
    font-weight: 600;
    letter-spacing: 0.06em;
  }
  .brand__dot {
    border-radius: 50%;
    background: var(--brand-red);
    flex: none;
  }
  .services {
    text-align: center;
    font-weight: 400;
    letter-spacing: 0.04em;
    color: var(--ink);
  }
  .services__accent { color: var(--brand-red); }

  .card--front .identity { left: 50%; top: 50%; }
  .card--front .brand { font-size: 60px; gap: 18px; }
  .card--front .brand__dot { width: 44px; height: 44px; }
  .card--front .services { margin-top: 14px; font-size: 24px; }

  .card--back .identity { left: 201px; top: 380px; }
  .card--back .brand { font-size: 36px; gap: 12px; }
  .card--back .brand__dot { width: 26px; height: 26px; }
  .card--back .services { margin-top: 8px; font-size: 18px; line-height: 1.35; }

  .back-shapes {
    position: absolute;
    inset: 0;
    width: 100%;
    height: 100%;
  }
  .contact {
    position: absolute;
    color: var(--white);
    white-space: nowrap;
  }
  .contact__name   { left: 497px; top: 158px; font-size: 50px; }
  .contact__phone  { left: 500px; top: 312px; font-size: 32px; }
  .contact__email  { left: 500px; top: 352px; font-size: 32px; }
  .contact__abn    { left: 460px; top: 426px; font-size: 44px; }
</style>
</head>
<body>

<section class="card card--front">
  <div class="identity">
    <div class="brand">
      <span class="brand__dot"></span>
      <span class="brand__name">ATELIER MIROU</span>
    </div>
    <p class="services">Traditional French Food <span class="services__accent">·</span> Cocktail Party <span class="services__accent">·</span> Catering</p>
  </div>
</section>

<section class="card card--back">
  <svg class="back-shapes" viewBox="0 0 896 517" preserveAspectRatio="none" aria-hidden="true">
    <defs>
      <linearGradient id="swoosh" x1="0" y1="0" x2="0" y2="1">
        <stop offset="0" stop-color="var(--orange-light)"/>
        <stop offset="1" stop-color="var(--orange-deep)"/>
      </linearGradient>
    </defs>
    <rect class="back-shapes__navy" width="896" height="517" fill="var(--navy)"/>
    <path class="back-shapes__swoosh" d="M0,0 H418 C525,150 515,370 350,517 H0 Z" fill="url(#swoosh)"/>
    <path class="back-shapes__white" d="M0,0 H411 C500,150 488,360 298,517 H0 Z" fill="var(--white)"/>
  </svg>

  <div class="identity">
    <div class="brand">
      <span class="brand__dot"></span>
      <span class="brand__name">ATELIER MIROU</span>
    </div>
    <p class="services">Traditional French Food<br>Cocktail Party &amp; Catering</p>
  </div>

  <p class="contact contact__name">Julien Maraval</p>
  <p class="contact contact__phone">Phone: 0491 237 750</p>
  <p class="contact contact__email">Email : julien@mirou.fr</p>
  <p class="contact contact__abn">ABN 98765432101</p>
</section>

</body>
</html>
```